elec business card

hi all

Im after a new age looking business card with my company logo on it

must include these details, I would like the PH and Email to be symbols

If the colours used for card could be kept within the colours used in logo that I have supplied that would be great, if another colour is to be used dark grey would be ok. no light bulbs etc thanks

Details below to be incorporated on card

Dorian Pellow

Lic E781392

PH 0219467318

E info@brightwayelectrical.example.nz

Domestic Commercial Industrial Electricians

```html
<!DOCTYPE html>
<html lang="en">
<head>
<meta charset="utf-8">
<title>Brightway Electrical – Business Card Front</title>
<link rel="stylesheet" href="https://fonts.googleapis.com/css2?family=Open+Sans:wght@400;700&display=swap">
<style>
  :root {
    --brand-blue: #1176b9;
    --charcoal: #2a313b;
    --ink: #111111;
    --paper: #ffffff;
  }
  html, body {
    margin: 0;
    padding: 0;
    overflow: hidden;
    background: var(--paper);
  }
  .card {
    position: relative;
    width: 1200px;
    height: 686px;
    box-sizing: border-box;
    border: 2px solid var(--brand-blue);
    background: var(--paper);
    overflow: hidden;
    font-family: "Open Sans", Arial, sans-serif;
  }
  .base-bands {
    position: absolute;
    left: 0;
    top: 0;
    width: 1196px;
    height: 682px;
  }
  .brand {
    position: absolute;
    left: 0;
    right: 0;
    top: 178px;
    display: flex;
    flex-direction: column;
    align-items: center;
  }
  .brand-dot {
    width: 70px;
    height: 70px;
    border-radius: 50%;
    background: var(--brand-blue);
    margin-bottom: 26px;
  }
  .brand-name {
    margin: 0;
    color: var(--brand-blue);
    font-weight: 700;
    font-size: 46px;
    letter-spacing: 3px;
    text-transform: uppercase;
    line-height: 1;
  }
  .services {
    position: absolute;
    left: 0;
    right: 0;
    top: 392px;
    margin: 0;
    text-align: center;
    color: var(--ink);
    font-weight: 400;
    font-size: 31px;
    line-height: 1.2;
  }
</style>
</head>
<body>
  <main class="card">
    <svg class="base-bands" viewBox="0 0 1196 682" aria-hidden="true">
      <polygon fill="var(--charcoal)" points="0,512 598,570 1196,512 1196,682 0,682"/>
      <polygon fill="var(--brand-blue)" points="352,546 598,570 859,546 788,678 408,678"/>
    </svg>

    <div class="brand">
      <span class="brand-dot"></span>
      <h1 class="brand-name">Brightway Electrical</h1>
    </div>

    <p class="services">Domestic Commercial Industrial Electricians</p>
  </main>
</body>
</html>
```